Producer Needs a Movie Poster for a Dramatic Film

We need a movie poster for a new dramatic film called "Past the Lantern".
Synopisis: A young drug addict (cocaine and alcohol), ROSS PENDRY, has hit rock bottom after a continuous downward spiral of alcoholism and drug abuse, leaving him with nothing to live for. His ex-girlfriend left him. His best friend doesn’t want anything to do with him. Unable to rehabilitate himself after multiple attempts, he attempts suicide (Jumping off of a high-rise apartment building).
We want the poster to give the dark feel of the film. It should be serious and personable.
We want the three lead actors to be listed on the top of the poster from left to right (Gregory Lint, Miriam Kessub, Osric Demmelby).
The title of the film, Past the Lantern, should be in the center of the poster.
We want "Coming Soon" centered on the bottom of the poster.

No pictures will be provided for this poster, so be creative and make something special for us to use. We're looking for a variety of good ideas.

We're excited to see what you come up with!

Please, make sure you provide us with files we can easily use. Also, we would like a copy of the film title in a separate file for easy use as well. So, two files total (One with the poster, One with just the film title by itself).

Industry/Entity Type

Movie

Requirements
Must have
• We want the three lead actors to be listed on the top of the poster from left to right (Gregory Lint, Miriam Kessub, Osric Demmelby).
• The title of the film, Past the Lantern, should be in the center of the poster.
• We want "Coming Soon" centered on the bottom of the poster.
• Please, make sure you provide us with files we can easily use. Also, we would like a copy of the film title in a separate file for easy use as well. So, two files total (One with the poster, One with just the film title by itself).
Should not have
• Should not have a person on the poster unless they are unrecognizable and you can't see any characteristics. We can't have someone on the poster who won't be in the movie.
• Don't put each locations that won't be in the film either. It takes place in LOs Angeles. Mostly on a high-rise apartment building rooftop.

```html
<!DOCTYPE html>
<html lang="en">
<head>
<meta charset="utf-8">
<title>Past the Lantern — Poster Variations</title>
<link rel="stylesheet" href="https://fonts.googleapis.com/css2?family=Bebas+Neue&display=swap">
<style>
  :root {
    --page-bg: #ffffff;
    --ink-white: #ffffff;
    --night: #0c0214;
    --night-mid: #2a0718;
    --window-red: #ff2a33;
    --figure-amber: #ffa42a;
    --mono-black: #050505;
    --mono-mid: #3a3a3a;
    --mono-grey: #7a7a7a;
    --mono-light: #b0b0b0;
  }
  * { margin: 0; padding: 0; box-sizing: border-box; }
  html, body {
    width: 1200px;
    height: 919px;
    overflow: hidden;
    background: var(--page-bg);
  }
  .presentation {
    position: relative;
    width: 1200px;
    height: 919px;
  }
  .poster {
    position: absolute;
    top: 42px;
    width: 533px;
    height: 806px;
  }
  .poster--colour { left: 27px; }
  .poster--mono { left: 618px; }
  .poster svg { display: block; width: 100%; height: 100%; }
  .poster text { font-family: "Bebas Neue", "Oswald", sans-serif; }
  .cast-name { font-size: 19px; letter-spacing: 1.2px; }
  .title-word { fill: var(--ink-white); }
  .release-line {
    font-size: 38px;
    letter-spacing: 10px;
    fill: var(--ink-white);
    stroke: #000000;
    stroke-width: 2px;
    paint-order: stroke;
  }
  .poster--colour .bg { fill: var(--night); }
  .poster--mono .bg { fill: var(--mono-black); }
  .poster--colour .cast-lead { fill: var(--ink-white); }
  .poster--colour .cast-second { fill: var(--window-red); }
  .poster--colour .cast-third { fill: var(--figure-amber); }
  .poster--mono .cast-lead { fill: var(--ink-white); }
  .poster--mono .cast-second { fill: var(--mono-grey); }
  .poster--mono .cast-third { fill: var(--mono-light); }
</style>
</head>
<body>
<main class="presentation">

  <article class="poster poster--colour">
    <svg viewBox="0 0 533 806" xmlns="http://www.w3.org/2000/svg">
      <defs>
        <linearGradient id="cityGlowColour" x1="0" y1="0" x2="1" y2="1">
          <stop offset="0" stop-color="#ffa42a" stop-opacity="0.85"/>
          <stop offset="0.35" stop-color="#3a0a1c"/>
          <stop offset="0.7" stop-color="#b8182a"/>
          <stop offset="1" stop-color="#ff2a33"/>
        </linearGradient>
      </defs>
      <rect class="bg" width="533" height="806"/>
      <g role="img" aria-label="Rooftop scene: amber silhouette of a man in a long coat standing before red-lit high-rise apartment windows">
        <rect x="0" y="180" width="533" height="626" fill="url(#cityGlowColour)" opacity="0.9"/>
      </g>
      <text class="cast-name cast-lead" x="52" y="41">GREGORY LINT</text>
      <text class="cast-name cast-third" x="322" y="41">OSRIC DEMMELBY</text>
      <text class="cast-name cast-second" x="205" y="64">MIRIAM KESSUB</text>
      <text class="title-word" x="63" y="330" font-size="230" textLength="255" lengthAdjust="spacingAndGlyphs">PAST</text>
      <text class="title-word" x="337" y="291" font-size="94" textLength="138" lengthAdjust="spacingAndGlyphs">THE</text>
      <text class="title-word" x="48" y="438" font-size="188" textLength="440" lengthAdjust="spacingAndGlyphs">LANTERN</text>
      <text class="release-line" x="266" y="696" text-anchor="middle">COMING SOON</text>
    </svg>
  </article>

  <article class="poster poster--mono">
    <svg viewBox="0 0 533 806" xmlns="http://www.w3.org/2000/svg">
      <defs>
        <linearGradient id="cityGlowMono" x1="0" y1="0" x2="1" y2="1">
          <stop offset="0" stop-color="#b0b0b0" stop-opacity="0.85"/>
          <stop offset="0.35" stop-color="#1c1c1c"/>
          <stop offset="0.7" stop-color="#4a4a4a"/>
          <stop offset="1" stop-color="#7a7a7a"/>
        </linearGradient>
      </defs>
      <rect class="bg" width="533" height="806"/>
      <g role="img" aria-label="Rooftop scene in greyscale: silhouette of a man in a long coat standing before lit high-rise apartment windows">
        <rect x="0" y="180" width="533" height="626" fill="url(#cityGlowMono)" opacity="0.9"/>
      </g>
      <text class="cast-name cast-lead" x="52" y="41">GREGORY LINT</text>
      <text class="cast-name cast-third" x="322" y="41">OSRIC DEMMELBY</text>
      <text class="cast-name cast-second" x="205" y="64">MIRIAM KESSUB</text>
      <text class="title-word" x="63" y="330" font-size="230" textLength="255" lengthAdjust="spacingAndGlyphs">PAST</text>
      <text class="title-word" x="337" y="291" font-size="94" textLength="138" lengthAdjust="spacingAndGlyphs">THE</text>
      <text class="title-word" x="48" y="438" font-size="188" textLength="440" lengthAdjust="spacingAndGlyphs">LANTERN</text>
      <text class="release-line" x="266" y="696" text-anchor="middle">COMING SOON</text>
    </svg>
  </article>

</main>
</body>
</html>
```